Killer Webpage Design

I currently have a self-hosted webpage through wordpress at www.varnetpixel.com - the content is complete and I'm happy with this but I need it designed (no coding) to complete my requirements. I'm happy to take designs which are non-Wordpress if there is specific advantage in this.

My full branding logos are attached along with color files. My main aim is consistent branding across all areas (social media, business cards, emails, websites). I have the rest running but am not happy with the available default selections from Wordpress.

I would prefer to use the darker blue version of the logo as I feel this has more standout in online media, however I would appreciate submissions with both variants to help me choose.

With the homepage I will also want to see blog pages and category pages designed but this can come after I have selected a design to go with,

Sites that I like and are related to my business include the following:
http://www.plumtally.com/au/accounting-software/
http://www.taskbrindle.com/home.aspx
https://tillnorth.com/register
Updates

Apologies for the confusion - to clarify for designers I am looking for design only, no coding.

FYI - i have now uploaded business cards for an idea of the contemporary style of design completed so far.

Target Market(s)

small to medium business. Not systemised but looking for help and support.

Industry/Entity Type

Business

Requirements
Must have
• I'm looking for a minimalist professional page, with the ability to easily add new sections when required. I will also need a CMS to add blog posts on the go, with the same features that it currently has (comments, social logon etc)

```html
<!DOCTYPE html>
<html lang="en">
<head>
<meta charset="utf-8">
<title>Varnet Pixel – Specialist Business Consultants</title>
<link href="https://fonts.googleapis.com/css2?family=PT+Sans:wght@400;700&family=Open+Sans:wght@400;700&display=swap" rel="stylesheet">
<style>
:root{
  --navy:#03283a;
  --navy-soft:#0b3d52;
  --teal:#0abac4;
  --teal-text:#13b1bd;
  --white:#ffffff;
  --grey-text:#8c8c8c;
  --dark-text:#1d2a30;
  --panel:#efefef;
  --nav-text:#6d6d6d;
}
*{margin:0;padding:0;box-sizing:border-box}
html,body{width:1200px;height:1051px;overflow:hidden;background:var(--white)}
body{font-family:"PT Sans",sans-serif;position:relative}
a{text-decoration:none;color:inherit}

.site-header{position:absolute;left:0;top:0;width:1200px;height:106px;background:var(--navy)}
.brand{position:absolute;left:189px;top:34px;display:flex;align-items:center;gap:10px}
.brand-dot{width:38px;height:38px;border-radius:50%;background:var(--teal)}
.brand-name{font-family:"PT Sans",sans-serif;font-weight:700;font-size:28px;color:var(--white);letter-spacing:-.3px}
.social{position:absolute;left:877px;top:34px;display:flex;gap:10px}
.social span{width:38px;height:38px;border-radius:50%;background:var(--navy-soft);display:block}

.main-nav{position:absolute;left:0;top:106px;width:1200px;height:40px;background:var(--white)}
.main-nav ul{list-style:none;position:absolute;left:198px;top:0;height:40px;display:flex;align-items:center;font-family:"Open Sans",sans-serif;font-size:11px;color:var(--nav-text);text-transform:uppercase}
.main-nav li{display:flex;align-items:center}
.main-nav li+li::before{content:"";width:1px;height:13px;background:#b5b5b5;margin:0 16px}
.main-nav .current{color:var(--teal-text)}

.hero{position:absolute;left:0;top:146px;width:1200px;height:409px;background:var(--teal)}
.hero-title{position:absolute;left:187px;top:106px;color:var(--white);font-family:"Open Sans",sans-serif;line-height:1}
.hero-title .light{display:block;font-size:27px;font-weight:400;letter-spacing:-.4px}
.hero-title .bold{display:block;font-size:35px;font-weight:700;margin-top:2px;letter-spacing:.3px}
.hero-quote{position:absolute;left:188px;top:176px;width:260px;color:var(--white);font-family:"Open Sans",sans-serif;font-size:13px;line-height:19px;padding-left:22px}
.hero-quote::before{content:"\201C";position:absolute;left:0;top:2px;font-size:26px;line-height:1;font-weight:700}
.hero-quote .close{font-size:24px;font-weight:700;line-height:0;vertical-align:-8px;margin-left:4px}
.hero-visual{position:absolute;left:467px;top:38px;width:544px;height:322px;border-radius:10px 10px 4px 4px;background:linear-gradient(160deg,#4f6a7a 0%,#8a8f8e 45%,#c9b89a 75%,#d8d8d8 100%)}
.slider-dots{position:absolute;left:723px;top:369px;display:flex;gap:8px}
.slider-dots span{width:12px;height:12px;border-radius:50%;background:var(--white)}
.slider-dots .active{background:transparent;border:2px solid var(--white)}

.section-heading{display:flex;align-items:center;gap:8px;font-family:"PT Sans",sans-serif;font-weight:700;font-size:18px;color:var(--teal-text);text-transform:uppercase}
.section-heading .mark{width:14px;height:14px;border-radius:50%;background:#d9693a;flex:none;margin-right:6px}

.welcome{position:absolute;left:189px;top:589px;width:526px}
.welcome .section-heading{margin-bottom:15px}
.welcome-photo{float:left;width:208px;height:143px;margin:0 14px 2px 0;background:linear-gradient(135deg,#e9e4dc 0%,#7c8690 50%,#3c4248 100%)}
.welcome p{font-size:12.2px;line-height:17.1px;color:var(--grey-text)}

.sidebar{position:absolute;left:737px;top:570px;width:274px;height:445px;background:var(--panel);border-radius:3px;z-index:2}
.widget{padding:20px 17px 0 17px;position:relative}
.widget .arrows{position:absolute;right:18px;top:24px;width:20px;height:14px}
.widget h4{font-weight:400;font-size:12px;color:var(--dark-text);margin-top:17px}
.widget p{font-size:11.7px;line-height:17.1px;color:var(--grey-text);margin-top:5px}
.widget .entry+.entry h4{margin-top:20px}
.widget.comments{border-top:1px solid #d6d6d6;margin-top:15px;padding-top:20px}

.site-footer{position:absolute;left:0;top:936px;width:1200px;height:115px;background:var(--navy)}
.footer-links{position:absolute;left:187px;top:26px;font-size:11.5px;line-height:17px;color:var(--teal-text)}
.footer-links .sep{margin:0 12px;color:var(--teal-text)}
.copyright{position:absolute;left:187px;top:64px;font-size:11.5px;color:var(--white)}
.footer-brand{position:absolute;left:608px;top:24px;display:flex;flex-direction:column;align-items:center;gap:6px}
.footer-brand .brand-dot{width:28px;height:28px;background:#1f7f8c}
.footer-brand .brand-name{font-size:18px;color:#9fb6bf}
</style>
</head>
<body>

<header class="site-header">
  <a class="brand" href="#"><span class="brand-dot"></span><span class="brand-name">VarnetPixel</span></a>
  <div class="social" aria-label="Social links"><span></span><span></span><span></span></div>
</header>

<nav class="main-nav">
  <ul>
    <li class="current">Software Training and Implementation</li>
    <li>Project Management</li>
    <li>Business Process Analysis</li>
    <li>Blog</li>
    <li>About Us</li>
    <li>Contact</li>
  </ul>
</nav>

<section class="hero">
  <h1 class="hero-title"><span class="light">SPECIALIST BUSINESS</span><span class="bold">CONSULTANTS</span></h1>
  <blockquote class="hero-quote">Whatever the mind of man can conceive and believe, it can achieve. Thoughts are things! And powerful things at that, when mixed with definiteness of purpose, and burning desire, can be translated into riches<span class="close">&#8221;</span></blockquote>
  <div class="hero-visual" role="img" aria-label="Laptop showing three business consultants shaking hands at a meeting table"></div>
  <div class="slider-dots"><span class="active"></span><span></span><span></span></div>
</section>

<main class="welcome">
  <h2 class="section-heading"><span class="mark"></span>Welcome to Varnet Pixel</h2>
  <div class="welcome-photo" role="img" aria-label="Business team reviewing documents around a laptop"></div>
  <p>Cloud computing spending is due to account for a third of annual IT expenditure growth by the end of 2013. Every year the range of cloud software systems gets bigger, now including Plumtally Accounting, Gridmail Apps for Business, Jobcrate Job Management Software, Northdesk Workspace, Taskloom Project Manager and many more. Signing up for cloud software is only the first part of the process, and then it has to be implemented into your business. That's where Varnet Pixel comes in. Formed in 2011, and with a history in cloud computing, implementation and support, we know there's much more to software implementation and effective business use than the purchase. We can assist by providing an external resource to assist with implementation, as well as getting the right processes post-implementation. Cloud software brings with it a huge array of benefits and efficiencies, but only if resourced and implemented correctly. Do you have somebody in your business that you can afford not to work in their role in order to implement? Having seen the negative impact this can have, we are there to help.</p>
</main>

<aside class="sidebar">
  <section class="widget">
    <h3 class="section-heading"><span class="mark"></span>Blog Post</h3>
    <svg class="arrows" viewBox="0 0 20 14" aria-hidden="true"><path d="M7 1 1 7l6 6M13 1l6 6-6 6" fill="none" stroke="#3b5866" stroke-width="1.4"/></svg>
    <div class="entry"><h4>Northdesk Mail to Gridmail Apps</h4><p>With Northdesk making big strides recently to move their huge office suite into the cloud,</p></div>
    <div class="entry"><h4>So why Cloud Software...?</h4><p>Cloud software is a massive area of the market and has emerged as a viable choice for many</p></div>
  </section>
  <section class="widget comments">
    <h3 class="section-heading"><span class="mark"></span>Recent Comments</h3>
    <svg class="arrows" viewBox="0 0 20 14" aria-hidden="true"><path d="M7 1 1 7l6 6M13 1l6 6-6 6" fill="none" stroke="#3b5866" stroke-width="1.4"/></svg>
    <div class="entry"><h4>Northdesk Mail to Gridmail Apps</h4><p>Lorem Ipsum is simply dummy text of the printing and typesetting industry. Lorem Ipsum has been the industry's standard dummy text ever since the 1500s, when an unknown printer took a galley of type and scrambled it to make a type specimen book. It has survived not only five centuries,</p></div>
  </section>
</aside>

<footer class="site-footer">
  <nav class="footer-links">
    <div>Home<span class="sep">|</span>Software Training and Implementation<span class="sep">|</span>Blog<span class="sep">|</span>About Us</div>
    <div>Project Management<span class="sep">|</span>Business Process Analysis<span class="sep">|</span>Contact us</div>
  </nav>
  <p class="copyright">Copyright © 2013 Varnet Pixel All right reserved.&nbsp; Powered by</p>
  <div class="footer-brand"><span class="brand-dot"></span><span class="brand-name">VarnetPixel</span></div>
</footer>

</body>
</html>
```